New Template, new corporate image Quelmoro 2022

New template designs for google slides or PowerPoint. Match to new corporate image. The new website www.quelmoro-mx.com Needs to match our new version. Technology and Artificial Intelligence elements to reflect our type of work.
We are adding old version of template and will send elements for the new corporate images.
Please consider our website as the main corporate image.
Our templates are being used on customer presentations, webminars, internal work only.
We have our main name of company Quelmoro. Quelmoro has to be in all the templates.
Secondary logo or branded service is: Calvindar.

Target Market(s)

Industrial users. Asset managers. Corporate visitors and customers.

Industry/Entity Type

Automotive. Chemical. Food and Beverage. Manufacturing

Other font styles liked:
• GE INSPIRA. RALEWAY

Colors
0054AA
0677BA
7BADD7
CADEEF
E8F1F8

Requirements
Must have
• Match to our elements on the new image. Use Brain Icons. Chips icons to connect equipments with software and control. Innovation.
Nice to have
• Unique images, machine images. Connecting machines and data elements. Template version for google slides. Image for industrial software for control equipment and saving money to manufacturers. Segments: Automotive, Chemical, Food and Beverages, Mining and pharmaceutical, Energy Management
Should not have
• old elements. not to much images of medical devices. Do not seems like a hospital.

```html
<!DOCTYPE html>
<html lang="en">
<head>
<meta charset="utf-8">
<title>Quelmoro Slide Template – Part 2</title>
<link href="https://fonts.googleapis.com/css2?family=Montserrat:wght@400;500;600;700&display=swap" rel="stylesheet">
<style>
:root{
  --blue:#0054AA;
  --blue-mid:#0677BA;
  --blue-soft:#7BADD7;
  --blue-pale:#CADEEF;
  --blue-mist:#E8F1F8;
  --ink:#3a3a3a;
  --footer:#262626;
  --canvas:#e5e4e2;
  --card:#f2f2f2;
  --rule:#d0d0d0;
}
*{margin:0;padding:0;box-sizing:border-box}
html,body{width:1200px;height:1200px;overflow:hidden;background:var(--canvas);font-family:'Montserrat',sans-serif;color:var(--ink)}
.canvas{position:relative;width:1200px;height:1200px}
.slide{position:absolute;width:533px;height:300px;background:#fff;overflow:hidden}
.slide-title{position:absolute;left:22px;top:22px;font-size:20px;font-weight:700;color:var(--blue);letter-spacing:.1px}
.footer{position:absolute;left:0;bottom:0;width:100%;height:22px;background:var(--footer)}
.footer svg.stripe{position:absolute;left:420px;top:0}
.footer-meta{position:absolute;left:22px;top:7px;font-size:6px;color:#ddd;font-weight:500}
.footer-meta .page{color:var(--blue-mid);font-weight:700;margin-right:3px}
.brand{position:absolute;right:22px;top:5px;font-size:9.5px;font-weight:600;color:var(--blue-mid)}
.sec-head{font-weight:700;color:var(--blue)}
/* About */
.hero{position:absolute;left:0;top:55px;width:533px;height:118px;background:linear-gradient(100deg,#0b1d33 0%,#10335c 45%,#0c4590 80%,#0a4b9c 100%)}
.hero-text{position:absolute;left:0;top:89px;width:533px;text-align:center;color:#fff}
.hero-text h3{font-size:14px;font-weight:700;margin-bottom:2px}
.hero-text p{font-size:12px;line-height:15px;font-weight:400}
.trio{position:absolute;left:0;top:190px;width:533px;display:flex;justify-content:space-between;padding:0 12px}
.trio-col{width:170px;text-align:center;height:64px}
.trio-col+.trio-col{border-left:1px solid var(--rule)}
.trio-col h4{font-size:11.5px;margin-top:4px}
.trio-col p{font-size:7.5px;line-height:9.5px;margin-top:2px}
/* Chart */
.copy{position:absolute;left:23px;width:230px}
.copy h4{font-size:11.5px}
.copy p{font-size:8.8px;line-height:10.6px;margin-top:2px}
.hrule{position:absolute;left:23px;top:155px;width:226px;height:1px;background:var(--rule)}
.vrule{position:absolute;left:280px;top:63px;width:1px;height:201px;background:var(--rule)}
.chart-title{position:absolute;left:348px;width:100px;top:66px;text-align:center;font-size:10px;font-weight:700;color:var(--blue)}
.donut{position:absolute;left:323px;top:85px}
.legend{position:absolute;left:318px;top:242px;font-size:7.5px;color:#666;display:flex;gap:8px;white-space:nowrap}
.legend i{display:inline-block;width:4px;height:4px;margin-right:2px;vertical-align:middle}
/* Services */
.cards{position:absolute;left:16px;top:63px;display:flex;gap:5px}
.card{width:121px;height:157px;background:var(--card);text-align:center}
.card-top{height:73px;background:var(--blue);display:flex;align-items:center;justify-content:center}
.card h4{font-size:11.5px;margin-top:10px}
.card p{font-size:7.8px;line-height:9.3px;margin-top:3px}
.services-note{position:absolute;left:0;top:232px;width:533px;text-align:center;font-size:8.5px;line-height:11px}
/* Table */
.data-table{position:absolute;left:22px;top:60px;width:490px;border-collapse:collapse;font-size:10.5px}
.data-table th{background:var(--blue);color:#fff;font-weight:700;text-align:left;height:31px;padding-left:4px}
.data-table td{height:31.4px;padding-left:4px;font-weight:400}
.data-table td:first-child{color:var(--blue);font-weight:700}
.data-table tr:nth-child(even) td{background:var(--card)}
.data-table tbody tr:last-child td{border-bottom:1.5px solid var(--blue)}
.data-table th:first-child,.data-table td:first-child{width:63px}
/* Map */
.map-area{position:absolute;left:40px;top:62px;width:453px;height:190px;border-radius:40px;background:radial-gradient(ellipse at center,#cfcfcf 0%,#d8d8d8 55%,#fff 100%)}
.pin{position:absolute;width:20px;height:20px;margin:-10px 0 0 -10px;border-radius:50%;background:var(--blue-mid);border:1.5px solid #fff;color:#fff;font-size:6.5px;font-weight:700;display:flex;align-items:center;justify-content:center}
.pin-label{position:absolute;width:90px}
.pin-label h5{font-size:7px;font-weight:700;color:var(--blue)}
.pin-label p{font-size:5.3px;color:#555;margin-top:2px}
.pin-label.right{text-align:right}
.part-label{position:absolute;left:54px;top:1046px;font-family:'Montserrat',sans-serif;font-size:108px;font-weight:700;color:#111;letter-spacing:-1px}
</style>
</head>
<body>
<div class="canvas">

<section class="slide" style="left:53px;top:46px">
  <h2 class="slide-title">About Us</h2>
  <div class="hero" role="img" aria-label="Photograph of Earth at night seen from orbit, deep blue tones"></div>
  <div class="hero-text">
    <h3>Section Header</h3>
    <p>Lorem ipsum dolor sit amet, consectetur adipiscing elit. Curabitur at fringilla velit.<br>In ac sagittis nulla. Nulla quis erat et ligula aliquam sagittis in viverra mauris.</p>
  </div>
  <div class="trio">
    <div class="trio-col"><h4 class="sec-head">Section Header</h4><p>Lorem ipsum dolor sit amet,<br>consecteturat es adipiscing elit.<br>Curabitur fringilla velit.</p></div>
    <div class="trio-col"><h4 class="sec-head">Section Header</h4><p>Lorem ipsum dolor sit amet,<br>consecteturat es adipiscing elit.<br>Curabitur fringilla velit.</p></div>
    <div class="trio-col"><h4 class="sec-head">Section Header</h4><p>Lorem ipsum dolor sit amet,<br>consecteturat es adipiscing elit.<br>Curabitur fringilla velit.</p></div>
  </div>
  <footer class="footer">
    <svg class="stripe" width="113" height="22"><polygon points="0,0 10,0 22,22 12,22" fill="var(--blue-mid)"/><polygon points="10,0 113,0 113,22 22,22" fill="#fff"/></svg>
    <div class="footer-meta"><span class="page">7</span>|&nbsp; Copyright © Quelmoro 2022</div>
    <div class="brand">Quelmoro</div>
  </footer>
</section>

<section class="slide" style="left:614px;top:46px">
  <h2 class="slide-title">Chart with Content</h2>
  <div class="copy" style="top:72px"><h4 class="sec-head">Section Header</h4><p>Donec vel suscipit purus, ultrices ornare neque.<br>Sed nec est a lacus lacinia venenatis non at est.<br>Vestibulum vitae lorem lectus. Phasellus gravida<br>mauris a sapien elementum malesuada.<br>Vestibulum ut urna eu dolor.</p></div>
  <div class="hrule"></div>
  <div class="copy" style="top:169px"><h4 class="sec-head">Section Header</h4><p>Lorem ipsum dolor sit amet, consectetur<br>adipiscing elit. Curabitur at fringilla velit.<br>In ac sagittis nulla. Nulla quis erat et ligula<br>aliquam sagittis in viverra mauris.<br>Pellentesque a hendrerit orci at.</p></div>
  <div class="vrule"></div>
  <div class="chart-title">Sales</div>
  <svg class="donut" width="150" height="150" viewBox="0 0 150 150">
    <g transform="rotate(-90 75 75)" fill="none" stroke-width="22">
      <circle cx="75" cy="75" r="64" stroke="var(--blue)" stroke-dasharray="229 173.1"/>
      <circle cx="75" cy="75" r="64" stroke="var(--blue-mid)" stroke-dasharray="96 306.1" stroke-dashoffset="-229"/>
      <circle cx="75" cy="75" r="64" stroke="var(--blue-soft)" stroke-dasharray="32.4 369.7" stroke-dashoffset="-325"/>
      <circle cx="75" cy="75" r="64" stroke="var(--blue-pale)" stroke-dasharray="44.7 357.4" stroke-dashoffset="-357.4"/>
    </g>
  </svg>
  <div class="legend"><span><i style="background:var(--blue)"></i>1st Qtr</span><span><i style="background:var(--blue-mid)"></i>2nd Qtr</span><span><i style="background:var(--blue-soft)"></i>3rd Qtr</span><span><i style="background:var(--blue-pale)"></i>4th Qtr</span></div>
  <footer class="footer">
    <svg class="stripe" width="113" height="22"><polygon points="0,0 10,0 22,22 12,22" fill="var(--blue-mid)"/><polygon points="10,0 113,0 113,22 22,22" fill="#fff"/></svg>
    <div class="footer-meta"><span class="page">9</span>|&nbsp; Copyright © Quelmoro 2022</div>
    <div class="brand">Quelmoro</div>
  </footer>
</section>

<section class="slide" style="left:53px;top:374px">
  <h2 class="slide-title">Services</h2>
  <div class="cards">
    <div class="card">
      <div class="card-top">
        <svg width="46" height="46" viewBox="0 0 46 46" fill="none" stroke="#fff" stroke-width="1.6"><circle cx="23" cy="23" r="21" fill="var(--blue-mid)"/><circle cx="23" cy="23" r="4" fill="#fff"/><circle cx="15" cy="15" r="3"/><circle cx="31" cy="14" r="3"/><circle cx="14" cy="30" r="3"/><circle cx="31" cy="31" r="3"/><path d="M17 17l4 4M29 16l-4 5M16 28l4-3M29 29l-4-4"/></svg>
      </div>
      <h4 class="sec-head">Section Header</h4><p>Lorem ipsum dolor sit<br>amet, consectetur at<br>es adipiscing elit.<br>Curabitur fringilla</p>
    </div>
    <div class="card">
      <div class="card-top">
        <svg width="46" height="46" viewBox="0 0 46 46" fill="none" stroke="#fff" stroke-width="1.6"><circle cx="23" cy="23" r="21" fill="var(--blue-mid)"/><rect x="14" y="13" width="18" height="13" rx="3"/><circle cx="19" cy="19" r="1.5" fill="#fff"/><circle cx="27" cy="19" r="1.5" fill="#fff"/><path d="M23 13v-3M12 19h2M32 19h2M18 26v6M23 26v8M28 26v6M15 32h3M28 32h3"/></svg>
      </div>
      <h4 class="sec-head">Section Header</h4><p>Lorem ipsum dolor sit<br>amet, consectetur at<br>es adipiscing elit.<br>Curabitur fringilla</p>
    </div>
    <div class="card">
      <div class="card-top">
        <svg width="46" height="46" viewBox="0 0 46 46" fill="none" stroke="#fff" stroke-width="1.6"><circle cx="23" cy="23" r="21" fill="var(--blue-mid)"/><path d="M25 10l-9 15h7l-3 11 10-16h-7z" stroke-linejoin="round"/></svg>
      </div>
      <h4 class="sec-head">Section Header</h4><p>Lorem ipsum dolor sit<br>amet, consectetur at<br>es adipiscing elit.<br>Curabitur fringilla</p>
    </div>
    <div class="card">
      <div class="card-top">
        <svg width="46" height="46" viewBox="0 0 46 46" fill="none" stroke="#fff" stroke-width="1.6"><circle cx="23" cy="23" r="21" fill="var(--blue-mid)"/><path d="M18 11h10v4l3 4v16H15V19l3-4z"/><path d="M15 19h16M22 24h5v7h-5z"/></svg>
      </div>
      <h4 class="sec-head">Section Header</h4><p>Lorem ipsum dolor sit<br>amet, consectetur at<br>es adipiscing elit.<br>Curabitur fringilla</p>
    </div>
  </div>
  <p class="services-note">Lorem ipsum dolor sit amet, consectetur adipiscing elit. Curabitur at fringilla velit. In ac sagittis nulla.<br>Nulla quis erat et ligula aliquam sagittis in viverra mauris. Pellentesque pharetra hendrerit orci at.</p>
  <footer class="footer">
    <svg class="stripe" width="113" height="22"><polygon points="0,0 10,0 22,22 12,22" fill="var(--blue-mid)"/><polygon points="10,0 113,0 113,22 22,22" fill="#fff"/></svg>
    <div class="footer-meta"><span class="page">10</span>|&nbsp; Copyright © Quelmoro 2022</div>
    <div class="brand">Quelmoro</div>
  </footer>
</section>

<section class="slide" style="left:614px;top:374px">
  <h2 class="slide-title">Table Slides</h2>
  <table class="data-table">
    <thead><tr><th>Data</th><th>Header</th><th>Header</th><th>Header</th><th>Header</th><th>Header</th><th>Header</th><th>Header</th></tr></thead>
    <tbody>
      <tr><td>Value</td><td>00</td><td>00</td><td>00</td><td>00</td><td>00</td><td>00</td><td>00</td></tr>
      <tr><td>Value</td><td>00</td><td>00</td><td>00</td><td>00</td><td>00</td><td>00</td><td>00</td></tr>
      <tr><td>Value</td><td>00</td><td>00</td><td>00</td><td>00</td><td>00</td><td>00</td><td>00</td></tr>
      <tr><td>Value</td><td>00</td><td>00</td><td>00</td><td>00</td><td>00</td><td>00</td><td>00</td></tr>
      <tr><td>Value</td><td>00</td><td>00</td><td>00</td><td>00</td><td>00</td><td>00</td><td>00</td></tr>
    </tbody>
  </table>
  <footer class="footer">
    <svg class="stripe" width="113" height="22"><polygon points="0,0 10,0 22,22 12,22" fill="var(--blue-mid)"/><polygon points="10,0 113,0 113,22 22,22" fill="#fff"/></svg>
    <div class="footer-meta"><span class="page">11</span>|&nbsp; Copyright © Quelmoro 2022</div>
    <div class="brand">Quelmoro</div>
  </footer>
</section>

<section class="slide" style="left:53px;top:700px">
  <h2 class="slide-title">Map Slide</h2>
  <div class="map-area" role="img" aria-label="Grey world map showing the continents"></div>
  <div class="pin" style="left:140px;top:141px">01</div>
  <div class="pin-label right" style="left:29px;top:134px"><h5>Section Header</h5><p>Lorem ipsum dolor sit amet.</p></div>
  <div class="pin" style="left:382px;top:115px">02</div>
  <div class="pin-label" style="left:402px;top:104px"><h5>Section Header</h5><p>Lorem ipsum dolor sit amet.</p></div>
  <div class="pin" style="left:267px;top:117px">03</div>
  <div class="pin-label" style="left:257px;top:84px"><h5>Section Header</h5><p>Lorem ipsum dolor sit amet.</p></div>
  <div class="pin" style="left:396px;top:223px">04</div>
  <div class="pin-label" style="left:416px;top:212px"><h5>Section Header</h5><p>Lorem ipsum dolor sit amet.</p></div>
  <div class="pin" style="left:259px;top:171px">05</div>
  <div class="pin-label" style="left:279px;top:160px"><h5>Section Header</h5><p>Lorem ipsum dolor sit amet.</p></div>
  <div class="pin" style="left:193px;top:203px">06</div>
  <div class="pin-label right" style="left:80px;top:194px"><h5>Section Header</h5><p>Lorem ipsum dolor sit amet.</p></div>
  <footer class="footer">
    <svg class="stripe" width="113" height="22"><polygon points="0,0 10,0 22,22 12,22" fill="var(--blue-mid)"/><polygon points="10,0 113,0 113,22 22,22" fill="#fff"/></svg>
    <div class="footer-meta"><span class="page">12</span>|&nbsp; Copyright © Quelmoro 2022</div>
    <div class="brand">Quelmoro</div>
  </footer>
</section>

<div class="part-label">PART 2</div>
</div>
</body>
</html>
```